Fresh pet feed direct from manufacturer to door step. Quality and Freshness un-surpassed in Industr

Need Business Card Design; leading into many other projects, for New Franchised Business Opportunity providing home delivery of fresh dog and cat feed (no emphasis needed for cat) direct from manufacturing facility. (no middle men or distributors) Food is Farm to Factory fresh. Our trademarked tagline is "Quality is our MAIN Ingredient ! "
Updates

Please take note of other contest for Facebook Cover and Profile Pic's

Target Market(s)

Dog and Cat owners

Industry/Entity Type

Pet

Contact Information for Business Card

Name, address, local phone, national 800 number, website, email address

Other font styles liked:
• follow that from logo

Requirements
Must have
• Our feed is made in Texas with ingredients sourced from local farms. We want to lean heavy on the Made in West Texas , ranch theme but that has a 'black label', 'vantrell', 'premium', 'high-end' look and feel
Nice to have
• maybe have an offer on card? 20% off with promo code "x" etc.. ?? just a thought...

```html
<!DOCTYPE html>
<html lang="en">
<head>
<meta charset="utf-8">
<title>Harlan's Premium – Business Card</title>
<link rel="stylesheet" href="https://fonts.googleapis.com/css2?family=Libre+Baskerville:wght@400;700&family=Arimo:wght@400&display=swap">
<style>
  :root {
    --page: #e9eaec;
    --card: #ffffff;
    --ink: #1f1c1d;
    --gold: #c8932a;
    --gold-light: #e8b84a;
    --paw: #ecd3a0;
    --text: #222222;
  }
  * { box-sizing: border-box; margin: 0; padding: 0; }
  html, body { width: 1200px; height: 1000px; overflow: hidden; }
  body {
    background: var(--page);
    font-family: "Arimo", Arial, sans-serif;
    position: relative;
  }
  .card {
    position: absolute;
    width: 525px;
    height: 300px;
    background: var(--card);
    box-shadow: 0 6px 18px rgba(0,0,0,0.15);
    overflow: hidden;
  }
  .card--front { left: 45px; top: 350px; }
  .card--back  { left: 630px; top: 350px; }

  .paw {
    position: absolute;
    width: 34px;
    height: 30px;
    background: var(--paw);
    border-radius: 45% 45% 50% 50%;
  }

  .brand {
    position: absolute;
    display: flex;
    align-items: center;
    gap: 12px;
    font-family: "Libre Baskerville", Georgia, serif;
    font-weight: 700;
    color: var(--ink);
    letter-spacing: 1px;
    white-space: nowrap;
    line-height: 1.15;
  }
  .brand__name { display: flex; flex-direction: column; }
  .brand__dot {
    width: 14px; height: 14px;
    border-radius: 50%;
    background: var(--gold);
    flex: none;
  }
  .card--front .brand { left: 150px; top: 108px; font-size: 34px; }
  .card--back .brand { left: 62px; top: 128px; font-size: 18px; gap: 10px; }
  .card--back .brand__dot { width: 11px; height: 11px; }

  .divider { position: absolute; left: 205px; top: 0; width: 60px; height: 300px; }

  .person { position: absolute; left: 265px; top: 34px; font-family: "Libre Baskerville", Georgia, serif; }
  .person__name { font-size: 21px; color: var(--ink); }
  .person__title { font-size: 15px; color: var(--gold); margin-top: 4px; }

  .contacts { position: absolute; left: 285px; top: 145px; list-style: none; }
  .contacts li {
    display: flex; align-items: center; gap: 10px;
    font-size: 13px; color: var(--text);
    height: 28px;
    white-space: nowrap;
  }
  .contacts svg { width: 24px; height: 24px; flex: none; }
</style>
</head>
<body>

<section class="card card--front" aria-label="Card front">
  <div class="paw" role="img" aria-label="Paw print decoration" style="left:28px;top:35px"></div>
  <div class="paw" role="img" aria-label="Paw print decoration" style="left:70px;top:120px"></div>
  <div class="paw" role="img" aria-label="Paw print decoration" style="left:40px;top:210px"></div>
  <div class="brand"><span class="brand__dot"></span><span class="brand__name"><span>HARLAN'S</span><span>PREMIUM</span></span></div>
</section>

<section class="card card--back" aria-label="Card back">
  <div class="paw" role="img" aria-label="Paw print decoration" style="left:40px;top:28px"></div>
  <div class="paw" role="img" aria-label="Paw print decoration" style="left:10px;top:110px"></div>
  <div class="paw" role="img" aria-label="Paw print decoration" style="left:45px;top:235px"></div>
  <div class="paw" role="img" aria-label="Paw print decoration" style="left:150px;top:262px"></div>
  <div class="brand"><span class="brand__dot"></span><span class="brand__name"><span>HARLAN'S</span><span>PREMIUM</span></span></div>

  <svg class="divider" viewBox="0 0 60 300" aria-hidden="true">
    <defs>
      <linearGradient id="goldLine" x1="0" y1="0" x2="0" y2="1">
        <stop offset="0" stop-color="#e8b84a" stop-opacity="0.2"/>
        <stop offset="0.5" stop-color="#d9a033"/>
        <stop offset="1" stop-color="#c07a18" stop-opacity="0.3"/>
      </linearGradient>
    </defs>
    <line x1="2" y1="0" x2="58" y2="300" stroke="url(#goldLine)" stroke-width="2"/>
  </svg>

  <div class="person">
    <div class="person__name">Wade Calder</div>
    <div class="person__title">President</div>
  </div>

  <ul class="contacts">
    <li>
      <svg viewBox="0 0 24 24" aria-hidden="true"><polygon points="12,1 15,8.5 23,9 17,14.5 19,23 12,18.5 5,23 7,14.5 1,9 9,8.5" fill="var(--ink)"/><path d="M8 14 L12 10 L16 14 M9.5 13 V16 H14.5 V13" fill="none" stroke="var(--gold-light)" stroke-width="1.3"/></svg>
      Your Address City, Country
    </li>
    <li>
      <svg viewBox="0 0 24 24" aria-hidden="true"><polygon points="12,1 15,8.5 23,9 17,14.5 19,23 12,18.5 5,23 7,14.5 1,9 9,8.5" fill="var(--ink)"/><path d="M9 10 Q9 16 15 16 L15 14.5 L13.5 13.8 L12.8 14.6 Q10.6 13.6 10.2 11.8 L11 11 L10.4 9.6 Z" fill="var(--gold-light)"/></svg>
      123 (45) 678 901
    </li>
    <li>
      <svg viewBox="0 0 24 24" aria-hidden="true"><polygon points="12,1 15,8.5 23,9 17,14.5 19,23 12,18.5 5,23 7,14.5 1,9 9,8.5" fill="var(--ink)"/><rect x="10" y="9" width="4.5" height="7.5" rx="0.8" fill="none" stroke="var(--gold-light)" stroke-width="1.2"/></svg>
      123 (45) 678 901
    </li>
    <li>
      <svg viewBox="0 0 24 24" aria-hidden="true"><polygon points="12,1 15,8.5 23,9 17,14.5 19,23 12,18.5 5,23 7,14.5 1,9 9,8.5" fill="var(--ink)"/><rect x="8.5" y="10.5" width="7" height="5" fill="none" stroke="var(--gold-light)" stroke-width="1.1"/><path d="M8.5 10.5 L12 13.5 L15.5 10.5" fill="none" stroke="var(--gold-light)" stroke-width="1.1"/></svg>
      infoyourdomain.com
    </li>
  </ul>
</section>

</body>
</html>
```